Wealth Education Business Needs Sharp Business Card Design

We need a business card design for a recently launched investor education business called Harbor Crest.

The final design should promote security, empowerment, self improvement and financial gain. The card will ideally promote the stature of the business.

For more information and colours please visit harborcrest.com.au

Target Market(s)

Corporate executives and high net worth individuals

Industry/Entity Type

Education

Contact Information for Business Card

Name
Position
Contact Address
Phone
Mobile
Email
Website

```html
<!DOCTYPE html>
<html lang="en">
<head>
<meta charset="utf-8">
<title>Harbor Crest — Business Card</title>
<link rel="stylesheet" href="https://fonts.googleapis.com/css2?family=Michroma&family=Raleway:wght@400;600&display=swap">
<style>
  :root {
    --canvas: #e9e6e1;
    --card: #f4f4f4;
    --card-shade: #e2e2e2;
    --teal: #0d6f6c;
    --sky: #1fa3e0;
    --charcoal: #3b3b3d;
    --steel: #a9abad;
    --ink: #2d2d2f;
    --white: #ffffff;
  }
  * { margin: 0; padding: 0; box-sizing: border-box; }
  html, body {
    width: 1057px; height: 1200px; overflow: hidden;
    background: var(--canvas);
    font-family: "Raleway", Arial, sans-serif;
  }
  .canvas {
    position: relative; width: 1057px; height: 1200px;
  }
  .card {
    position: absolute; left: 98px; width: 860px; height: 490px;
    box-shadow: 0 14px 34px rgba(0,0,0,.22);
    overflow: hidden;
  }
  /* Front */
  .card-front {
    top: 60px;
    background: var(--teal);
    padding: 16px;
  }
  .card-front .inner-frame {
    width: 100%; height: 100%;
    background: var(--sky);
    padding: 12px;
  }
  .card-front .face {
    width: 100%; height: 100%;
    background: linear-gradient(160deg, var(--white) 0%, var(--card) 55%, var(--card-shade) 100%);
    display: flex; align-items: center; justify-content: center; gap: 18px;
  }
  .brand-dot {
    width: 22px; height: 22px; border-radius: 50%; background: var(--teal);
  }
  .brand-name {
    font-family: "Michroma", Arial, sans-serif;
    font-size: 38px; letter-spacing: 6px; color: var(--teal);
  }
  /* Back */
  .card-back {
    top: 650px;
    background: linear-gradient(160deg, var(--white) 0%, var(--card) 55%, var(--card-shade) 100%);
  }
  .card-back svg.bands { position: absolute; inset: 0; }
  .back-brand {
    position: absolute; left: 60px; top: 90px;
    font-family: "Michroma", Arial, sans-serif;
    font-size: 40px; letter-spacing: 7px; color: var(--ink);
  }
  .identity {
    position: absolute; left: 60px; top: 338px; color: var(--white);
  }
  .person-name {
    font-family: "Michroma", Arial, sans-serif;
    font-size: 24px; letter-spacing: 3px;
  }
  .person-role {
    font-size: 14px; letter-spacing: 4px; margin-top: 6px; text-transform: uppercase;
  }
  .details {
    position: absolute; left: 60px; top: 408px;
    list-style: none; color: var(--white); font-size: 12px; letter-spacing: 1px;
  }
  .details li { display: flex; align-items: center; gap: 10px; height: 22px; }
  .icon-box {
    width: 14px; height: 14px; background: var(--white);
    display: flex; align-items: center; justify-content: center;
  }
  .phones {
    position: absolute; right: 46px; top: 268px;
    list-style: none; color: var(--white); font-size: 14px; letter-spacing: 2px;
  }
  .phones li { display: flex; align-items: center; gap: 12px; height: 30px; }
  .phones .icon-box { width: 18px; height: 18px; }
</style>
</head>
<body>
<main class="canvas">

  <section class="card card-front" aria-label="Card front">
    <div class="inner-frame">
      <div class="face">
        <span class="brand-dot"></span>
        <span class="brand-name">HARBOR CREST</span>
      </div>
    </div>
  </section>

  <section class="card card-back" aria-label="Card back">
    <svg class="bands" width="860" height="490" viewBox="0 0 860 490" aria-hidden="true">
      <polygon points="640,200 860,200 860,245 612,245" fill="var(--steel)"/>
      <polygon points="612,245 860,245 860,370 540,370" fill="var(--teal)"/>
      <polygon points="0,318 590,318 500,490 0,490" fill="var(--charcoal)"/>
      <polygon points="0,395 548,395 540,410 0,410" fill="#4a4a4d"/>
    </svg>

    <h1 class="back-brand">HARBOR CREST</h1>

    <div class="identity">
      <p class="person-name">DANIEL REEVE</p>
      <p class="person-role">Founder</p>
    </div>

    <ul class="details">
      <li>
        <span class="icon-box"><svg width="8" height="10" viewBox="0 0 8 10"><path d="M4 0a4 4 0 0 1 4 4c0 3-4 6-4 6S0 7 0 4a4 4 0 0 1 4-4z" fill="var(--charcoal)"/></svg></span>
        24 Quay Street, Sydney NSW 2000 Australia
      </li>
      <li>
        <span class="icon-box"><svg width="10" height="10" viewBox="0 0 10 10"><circle cx="5" cy="5" r="4" fill="none" stroke="var(--charcoal)" stroke-width="1.4"/></svg></span>
        www.harborcrest.com.au
      </li>
      <li>
        <span class="icon-box"><svg width="10" height="8" viewBox="0 0 10 8"><rect x=".5" y=".5" width="9" height="7" fill="none" stroke="var(--charcoal)"/><path d="M.5 .5 5 4.5 9.5 .5" fill="none" stroke="var(--charcoal)"/></svg></span>
        info@harborcrest.com.au
      </li>
    </ul>

    <ul class="phones">
      <li>
        <span class="icon-box"><svg width="10" height="10" viewBox="0 0 10 10"><path d="M2 0l2 2-1 1.5 3.5 3.5L8 6l2 2-1.5 2C4 10 0 6 0 1.5z" fill="var(--teal)"/></svg></span>
        014 220 5318
      </li>
      <li>
        <span class="icon-box"><svg width="8" height="11" viewBox="0 0 8 11"><rect x=".5" y=".5" width="7" height="10" rx="1" fill="none" stroke="var(--teal)"/><circle cx="4" cy="8.8" r=".8" fill="var(--teal)"/></svg></span>
        014 220 5319
      </li>
    </ul>
  </section>

</main>
</body>
</html>
```